Luxury packaging graphic design for a new Hair care elixir

We need a packaging design for a new product for our line extension of hair colouring. We have already a packaging that is very well received (all in pink) including all accesories and transport box (attached files).
For a new product - protein for the hair - we need a different design tapping into luxury segment.

Target Market(s)

This product is mainly for women between 25-65 that are looking forward to improve hair strukture and make hair looks better, nicer, softer, healthier. The product in the packaging could be used up to 2x times.

Industry/Entity Type

Hair And Beauty

Font styles to use
Serif
Sans Serif

Colors

Designer to choose colors to be used in the design.

Requirements
Must have
• The material of the packaging are carton/styropor/and glass (attached a picture of packaging design to be adapted). The components are quite small so the packaging plays a big role to increase the value of what it is inside. The packaging needs to be inline with our actual packaging designs and corporate identity as they may be delivered together so as an assamble it should look nice, beautiful and of high quality.
• The graphic design for the different components to be adapted are:
• - grapich design for outside box
• - graphic design for the inside bottles
• - graphic design for the flyer/instructions inside the box
Nice to have
• It needs to feel that the packaging is Wow! It is going to be delivered per post so there have to be a beautiful opening effect. Eventually to work with colours like black, white and gold would give a nice luxury feeling.
• The actual product inside is a concentrated protein component so it is very small, therefore the packaging should show that even if small it is an elixir for the hair.
Should not have
• a totally diffenet look as our actual designs.

```html
<!DOCTYPE html>
<html lang="en">
<head>
<meta charset="utf-8">
<title>nola vey – box dieline 170 x 170 x 40 mm</title>
<link rel="stylesheet" href="https://fonts.googleapis.com/css2?family=Arimo:wght@700&family=Playfair+Display:wght@700&family=Open+Sans:wght@400;600&display=swap">
<style>
  :root {
    --paper: #ffffff;
    --ink: #111111;
    --box-black: #0c0b08;
    --olive-dark: #1f1d08;
    --olive: #4a4210;
    --gold: #c9a53a;
    --gold-light: #e6c860;
    --fold-red: #b0281c;
  }
  html, body {
    margin: 0;
    padding: 0;
    width: 1182px;
    height: 1200px;
    overflow: hidden;
    background: var(--paper);
  }
  .sheet { display: block; width: 1182px; height: 1200px; }
  .spec-title {
    font-family: "Arimo", Arial, sans-serif;
    font-weight: 700;
    font-size: 38px;
    fill: var(--ink);
  }
  .fold-line { fill: none; stroke: var(--fold-red); stroke-width: 1; opacity: .8; }
  .cut-edge { fill: none; stroke: var(--box-black); stroke-width: 4; }
  .seal-disc { fill: var(--box-black); stroke: var(--gold); stroke-width: 2.5; }
  .brand-name {
    font-family: "Playfair Display", Georgia, serif;
    font-weight: 700;
    font-size: 44px;
    fill: var(--gold);
  }
  .info-panel { fill: var(--box-black); opacity: .92; }
  .info-brand {
    font-family: "Playfair Display", Georgia, serif;
    font-weight: 700;
    font-size: 26px;
    fill: var(--gold);
  }
  .info-head {
    font-family: "Open Sans", Arial, sans-serif;
    font-weight: 600;
    font-size: 8px;
    fill: var(--gold-light);
  }
  .info-copy {
    font-family: "Open Sans", Arial, sans-serif;
    font-weight: 400;
    font-size: 7.5px;
    fill: var(--gold-light);
  }
</style>
</head>
<body>
<svg class="sheet" viewBox="0 -12 1476 1499" xmlns="http://www.w3.org/2000/svg">
  <defs>
    <linearGradient id="wave-tones" x1="0" y1="0" x2="1" y2="1">
      <stop offset="0" stop-color="var(--olive-dark)"/>
      <stop offset=".35" stop-color="var(--olive)"/>
      <stop offset=".6" stop-color="var(--olive-dark)"/>
      <stop offset=".85" stop-color="#5a4c12"/>
      <stop offset="1" stop-color="var(--olive-dark)"/>
    </linearGradient>
    <radialGradient id="seal-sheen" cx=".5" cy=".4" r=".6">
      <stop offset="0" stop-color="#1b1a17"/>
      <stop offset="1" stop-color="#070706"/>
    </radialGradient>
  </defs>

  <text class="spec-title" x="35" y="53">L 170 x P 170 x A 40 mm.</text>

  <!-- tray base dieline -->
  <g class="tray-base">
    <polygon role="img" aria-label="Flowing gold wave line pattern on black"
      fill="url(#wave-tones)"
      points="313,488 707,488 707,530 745,545 790,600 820,640 835,665 860,650 935,650 940,675 980,675 980,1145 940,1145 935,1170 862,1170 850,1140 830,1180 790,1225 745,1270 742,1295 707,1300 707,1335 318,1335 313,1295 285,1290 283,1235 240,1225 200,1180 185,1145 173,1170 90,1170 80,1145 35,1145 35,680 80,680 90,650 160,655 165,680 178,685 195,640 235,600 270,545 283,538 313,530"/>
    <rect class="fold-line" x="203" y="705" width="617" height="420"/>
    <line class="fold-line" x1="303" y1="607" x2="720" y2="607"/>
    <line class="fold-line" x1="303" y1="1222" x2="720" y2="1222"/>
    <line class="fold-line" x1="303" y1="607" x2="303" y2="705"/>
    <line class="fold-line" x1="720" y1="607" x2="720" y2="705"/>
    <line class="fold-line" x1="303" y1="1125" x2="303" y2="1222"/>
    <line class="fold-line" x1="720" y1="1125" x2="720" y2="1222"/>

    <circle class="seal-disc" cx="512" cy="915" r="170" fill="url(#seal-sheen)"/>
    <text class="brand-name" x="512" y="930" text-anchor="middle">nola vey</text>
  </g>

  <!-- sleeve panel -->
  <g class="sleeve">
    <rect x="980" y="213" width="472" height="1124" fill="var(--box-black)"/>
    <rect role="img" aria-label="Flowing gold wave line pattern on black"
      x="986" y="219" width="460" height="1112" fill="url(#wave-tones)"/>
    <line class="fold-line" x1="986" y1="685" x2="1446" y2="685"/>
    <line class="fold-line" x1="986" y1="785" x2="1446" y2="785"/>
    <line class="fold-line" x1="986" y1="1210" x2="1446" y2="1210"/>
    <rect class="cut-edge" x="980" y="213" width="472" height="1124"/>

    <g class="info-block" transform="rotate(180 1216 995)">
      <rect class="info-panel" x="1012" y="845" width="408" height="300"/>
      <text class="info-brand" x="1216" y="1122" text-anchor="middle">nola vey</text>
      <text class="info-head" x="1025" y="1103">How to use</text>
      <text class="info-copy" x="1025" y="1091">Apply to clean, towel-dried hair from mid-lengths to ends and leave on for ten minutes.</text>
      <text class="info-copy" x="1025" y="1080">Rinse well with lukewarm water and style as usual for a smooth, healthy finish.</text>
      <text class="info-head" x="1025" y="1055">Ingredients</text>
      <text class="info-copy" x="1025" y="1043">Aqua, hydrolyzed keratin, glycerin, panthenol, argan oil, parfum, citric acid.</text>
      <text class="info-copy" x="1025" y="1032">Store in a cool, dry place away from direct light.</text>
      <text class="info-head" x="1025" y="1000">What is inside?</text>
      <text class="info-copy" x="1025" y="988">A concentrated protein elixir made to restore strength, softness and shine to every strand of coloured hair.</text>
      <text class="info-copy" x="1025" y="977">Use one half of the vial per treatment and keep the rest sealed for a second care.</text>
    </g>
  </g>
</svg>
</body>
</html>
```